【依頼の目的/概要】
電子書籍(bookrie)の表紙デザインをお願いします。

【画像サイズ】※BRPより抜粋
表紙ファイルの理想的な寸法は2,560×1,600ピクセルです。
注:画像の寸法は10,000×10,000ピクセルです。

【タイトル】
資格試験 ゴールダッシュ・速習・楽々学習術

サブタイトル
通れる学び方

【著者】
行政書士 社会保険労務士
森川澄江

【本の内容】
行政書士試験の勉強を短期間で仕上げて、合格する勉強法を
書いた本です。

【デザイン要望】
特にこだわりません。
素敵なデザインの応募を楽しみにしています。
※次点、次々点の方への参加報酬を設定しました。

その他
必要な情報がありましたらお問い合わせください。

本を以下に添付します。
本文中にエクセルで作成した表を挿入します。

明るく見やすく、わかり易い表現が良かったです。

皆様お疲れ様でした。
T_okabe様には訂正を速攻して頂きありがとうございました。
最後まで迷いました。
皆様のご依頼が増えますことをご祈念申し上げます。

```html
<!DOCTYPE html>
<html lang="ja">
<head>
<meta charset="UTF-8">
<title>資格試験 ゴールダッシュ・速習・楽々学習術</title>
<link rel="stylesheet" href="https://fonts.googleapis.com/css2?family=Noto+Sans+JP:wght@700;900&family=Noto+Serif+JP:wght@700;900&display=swap">
<style>
  :root {
    --cover-bg: #cdbb87;
    --emblem-light: #efe7cc;
    --emblem-edge: #e2d6ad;
    --ink: #141414;
  }
  html, body {
    margin: 0;
    padding: 0;
    overflow: hidden;
    background: var(--cover-bg);
  }
  .cover {
    position: relative;
    width: 750px;
    height: 1200px;
    background: var(--cover-bg);
    overflow: hidden;
    font-family: "Noto Sans JP", sans-serif;
    color: var(--ink);
  }
  .series-title {
    position: absolute;
    top: 4px;
    left: 0;
    width: 100%;
    margin: 0;
    text-align: center;
    font-weight: 900;
    font-size: 150px;
    line-height: 1.1;
    letter-spacing: 6px;
  }
  .emblem-area {
    position: absolute;
    left: 100px;
    top: 225px;
    width: 550px;
    height: 550px;
    border-radius: 50%;
    background: radial-gradient(circle, var(--emblem-light) 0%, var(--emblem-light) 60%, var(--emblem-edge) 100%);
  }
  .dial-text {
    position: absolute;
    top: 340px;
    left: 0;
    width: 100%;
    text-align: center;
    font-weight: 900;
  }
  .main-title {
    margin: 0;
    font-size: 108px;
    line-height: 1.12;
    letter-spacing: 2px;
  }
  .tagline {
    margin: 18px 0 0;
    font-size: 64px;
    line-height: 1.18;
    font-weight: 900;
  }
  .subtitle {
    position: absolute;
    top: 908px;
    left: 0;
    width: 100%;
    margin: 0;
    text-align: center;
    font-size: 80px;
    font-weight: 700;
    line-height: 1.2;
  }
  .author {
    position: absolute;
    top: 1058px;
    left: 0;
    width: 100%;
    text-align: center;
    font-family: "Noto Serif JP", serif;
  }
  .author-credentials {
    margin: 0;
    font-size: 26px;
    font-weight: 700;
    letter-spacing: 1px;
  }
  .author-name {
    margin: 6px 0 0;
    font-size: 52px;
    font-weight: 900;
    letter-spacing: 8px;
  }
</style>
</head>
<body>
  <main class="cover">
    <h1 class="series-title">資格試験</h1>

    <div class="emblem-area" role="img" aria-label="時計の文字盤を思わせる放射状の装飾エンブレム"></div>

    <div class="dial-text">
      <h2 class="main-title">ゴール<br>ダッシュ</h2>
      <p class="tagline">速習・楽々<br>学習術</p>
    </div>

    <p class="subtitle">通れる学び方</p>

    <div class="author">
      <p class="author-credentials">行政書士 社会保険労務士</p>
      <p class="author-name">森川澄江</p>
    </div>
  </main>
</body>
</html>
```